Medical Practice Business Card

we need a business card for our new medical ophthalmology practice based in Needham Massachusetts. we are looking for a simple , modern and elegant design.
the card needs to contain the following
1- the logo of our practice (please see attached file)
2- the name of the practice : "Silver Birch Retina Care"
3- Doctor's Name: Tobias Rendell MD PhD
4- Specialty: Board-Certified Vitreoretinal Surgeon
5- practice address: 87 Larkspur Ave, Suite 210, Needham MA 02481
7- Office number: 617- 482 - 7730
8- fax number: 617- 391 - 2268
9- email: info@sbretinahub.example
10- website: www.sbretinahub.example

```html
<!DOCTYPE html>
<html lang="en">
<head>
<meta charset="utf-8">
<title>Silver Birch Retina Care – Business Card</title>
<link href="https://fonts.googleapis.com/css2?family=Cinzel:wght@600&family=Roboto:wght@400;500&display=swap" rel="stylesheet">
<style>
  :root{
    --navy:#1c2f6b;
    --navy-deep:#17275c;
    --royal:#0f4a98;
    --sky:#6fb3dc;
    --mid-blue:#2f6fb8;
    --ink:#4a4f5a;
    --paper:#ffffff;
    --stage:#e9ebef;
  }
  *{box-sizing:border-box;margin:0;padding:0}
  html,body{width:1200px;height:856px;overflow:hidden;background:var(--stage)}
  .stage{width:1200px;height:856px;display:flex;align-items:center;justify-content:center;gap:40px}
  .card{width:540px;height:310px;position:relative;overflow:hidden;box-shadow:0 10px 28px rgba(20,30,60,.18)}

  /* front */
  .card-front{background:var(--paper)}
  .doctor{position:absolute;left:34px;top:34px}
  .doctor-name{font-family:'Cinzel',serif;font-weight:600;font-size:25px;color:var(--navy);letter-spacing:.5px}
  .doctor-title{font-family:'Roboto',sans-serif;font-size:14px;color:var(--ink);margin-top:4px}
  .divider{position:absolute;left:34px;top:106px;width:430px;height:1.5px;background:var(--navy)}
  .contacts{position:absolute;left:34px;top:118px;list-style:none;font-family:'Roboto',sans-serif;font-size:15px;color:var(--ink)}
  .contacts li{display:flex;align-items:center;gap:9px;height:24px}
  .contacts svg{width:13px;height:13px;fill:var(--mid-blue)}
  .practice-mark{position:absolute;right:34px;top:122px;display:flex;align-items:center;gap:10px}
  .mark-circle{width:26px;height:26px;border-radius:50%;background:var(--navy);flex:none}
  .practice-name{font-family:'Roboto',sans-serif;font-weight:500;font-size:17px;color:var(--navy);line-height:1.25}
  .address{position:absolute;right:34px;top:196px;font-family:'Roboto',sans-serif;font-size:14.5px;color:var(--ink);text-align:right;line-height:1.4}
  .band{position:absolute;left:0;bottom:0;width:540px;height:70px}
  .website{position:absolute;right:34px;bottom:14px;font-family:'Roboto',sans-serif;font-weight:500;font-size:15px;color:#fff}

  /* back */
  .card-back{background:linear-gradient(160deg,var(--navy-deep) 0%,var(--royal) 100%);display:flex;align-items:center;justify-content:center;gap:14px}
  .card-back .mark-circle{width:38px;height:38px;background:#fff}
  .card-back .practice-name{color:#fff;font-size:26px}
</style>
</head>
<body>
<main class="stage">
  <section class="card card-front" aria-label="Business card front">
    <div class="doctor">
      <h1 class="doctor-name">Tobias Rendell MD PhD</h1>
      <p class="doctor-title">Board-Certified Vitreoretinal Surgeon</p>
    </div>
    <div class="divider"></div>
    <ul class="contacts">
      <li><svg viewBox="0 0 24 24" aria-hidden="true"><path d="M6.6 10.8a15 15 0 0 0 6.6 6.6l2.2-2.2c.3-.3.7-.4 1-.2 1.1.4 2.3.6 3.6.6.6 0 1 .4 1 1V20c0 .6-.4 1-1 1A17 17 0 0 1 3 4c0-.6.4-1 1-1h3.5c.6 0 1 .4 1 1 0 1.3.2 2.5.6 3.6.1.3 0 .7-.2 1z"/></svg>617- 482 - 7730</li>
      <li><svg viewBox="0 0 24 24" aria-hidden="true"><path d="M6 2h9l3 3v5H6zM3 10h18v9h-3v3H6v-3H3zm5 6v4h8v-4z"/></svg>617- 391 - 2268</li>
      <li><svg viewBox="0 0 24 24" aria-hidden="true"><path d="M2 5h20v14H2zm2 2v.5l8 5 8-5V7z"/></svg>info@sbretinahub.example</li>
    </ul>
    <div class="practice-mark">
      <span class="mark-circle"></span>
      <span class="practice-name">Silver Birch<br>Retina Care</span>
    </div>
    <p class="address">87 Larkspur Ave, Suite 210,<br>Needham MA 02481</p>
    <svg class="band" viewBox="0 0 540 70" preserveAspectRatio="none" aria-hidden="true">
      <polygon points="0,28 250,28 244,34 0,34" fill="var(--sky)"/>
      <polygon points="0,37 240,37 232,44 0,44" fill="var(--mid-blue)"/>
      <polygon points="0,48 228,48 258,20 540,20 540,70 0,70" fill="var(--navy)"/>
    </svg>
    <p class="website">www.sbretinahub.example</p>
  </section>

  <section class="card card-back" aria-label="Business card back">
    <span class="mark-circle"></span>
    <span class="practice-name">Silver Birch<br>Retina Care</span>
  </section>
</main>
</body>
</html>
```